The Founder Crossroads Book Cover

I need a Book Cover Design for a new book:
Title - "The Founder Crossroads"
Subtitle - "Lessons No Classroom Ever Gives You"
Author - "Marcus Halden"

Target Market(s)

Entrepreneur's and Small Business Owners

Industry/Entity Type

Entrepreneur

Font styles to use
Sans Serif

Requirements
Must have
• The branding colors should match our website (Black and accent color: #FBBC05)
• http://FounderCrossroads.example
• Secondary Subtile (top bar) on front of cover - "A Documentary"
• Back Cover: Brief description, author photo, and the ISBN Number
Nice to have
• A Detour Sign with the word "Detour" on it (or a sign with a "squiggly" line example) ... or a type of image that is on the bottom of Home page of website (road in wilderness).

```html
<!DOCTYPE html>
<html lang="en">
<head>
<meta charset="utf-8">
<title>The Founder Crossroads – Book Cover</title>
<link rel="stylesheet" href="https://fonts.googleapis.com/css2?family=Antonio:wght@200;400&family=Montserrat:wght@800&display=swap">
<style>
  :root {
    --backdrop: #959393;
    --accent: #fbbc05;
    --title-white: #eeeeee;
    --sky: #5f5616;
    --ridge: #6e1a10;
    --dune: #a8260e;
    --dune-deep: #8c1c0c;
    --ground: #b4521c;
    --road: #5a3a1c;
    --road-dark: #2a1a0c;
    --ink: #060402;
  }
  * { margin: 0; padding: 0; box-sizing: border-box; }
  html, body {
    width: 1200px; height: 1000px; overflow: hidden;
    background: var(--backdrop);
  }
  .cover {
    position: absolute; left: 300px; top: 38px;
    width: 597px; height: 923px; overflow: hidden;
    box-shadow: 0 2px 8px rgba(0,0,0,.35);
  }
  .cover-photo {
    position: absolute; inset: 0;
    background:
      radial-gradient(ellipse 60% 40% at 50% 75%, rgba(120,80,30,.55), transparent 70%),
      linear-gradient(180deg,
        var(--sky) 0%,
        var(--ridge) 8%,
        var(--dune-deep) 18%,
        var(--dune) 30%,
        var(--dune-deep) 41%,
        var(--ground) 44%,
        var(--ground) 52%,
        var(--road) 62%,
        var(--road-dark) 82%,
        var(--ink) 100%);
  }
  .kicker, .title-line, .subtitle, .author {
    position: absolute; left: 0; width: 100%; text-align: center;
    white-space: nowrap;
  }
  .kicker {
    top: 27px;
    font: 400 26px/1 "Antonio", sans-serif;
    color: #ffffff; letter-spacing: .5px;
  }
  .title-the {
    top: 132px;
    font: 800 29px/1 "Montserrat", sans-serif;
    color: var(--accent);
  }
  .title-founder {
    top: 150px;
    font: 200 112px/1 "Antonio", sans-serif;
    color: var(--title-white); letter-spacing: 1px;
  }
  .title-crossroads {
    top: 256px;
    font: 800 72px/1 "Montserrat", sans-serif;
    color: var(--accent); letter-spacing: -1px;
  }
  .subtitle {
    top: 330px;
    font: 400 36px/1 "Antonio", sans-serif;
    color: #ffffff;
  }
  .author {
    top: 845px;
    font: 400 40px/1 "Antonio", sans-serif;
    color: var(--accent);
  }
</style>
</head>
<body>
  <main class="cover">
    <div class="cover-photo" role="img" aria-label="Photograph of a straight desert road running toward red mountains under a dark sky"></div>
    <p class="kicker">A DOCUMENTARY</p>
    <h1>
      <span class="title-line title-the">THE</span>
      <span class="title-line title-founder">FOUNDER</span>
      <span class="title-line title-crossroads">CROSSROADS</span>
    </h1>
    <p class="subtitle">LESSONS NO CLASSROOM EVER GIVES YOU</p>
    <p class="author">MARCUS HALDEN</p>
  </main>
</body>
</html>
```